Lumo Vance IT company Soho london Stationary

We've just had a new logo designed on Gallow Pier and we now need some Stationary to go with it.
We're a small IT support firm supporting Design companies in Soho London. Most of our clients work on Vorls and a relatively creative so we want a relatively informal design on our stationary to reflect this.
We'd like to stick with the green in the logo but we're not adverse to adding another few colours to the palette.
Please see the attached file for our logo and not our website.

It Company

```html
<!DOCTYPE html>
<html lang="en">
<head>
<meta charset="utf-8">
<title>Lumo Vance Stationery</title>
<link href="https://fonts.googleapis.com/css2?family=Source+Sans+3:wght@400;600&display=swap" rel="stylesheet">
<style>
  :root {
    --green: #c1d73a;
    --ink: #111111;
    --text: #2b2b2b;
    --paper: #ffffff;
    --backdrop: #4a3d3d;
  }
  * { box-sizing: border-box; margin: 0; padding: 0; }
  html, body { width: 1200px; height: 841px; overflow: hidden; }
  body {
    position: relative;
    background: var(--backdrop);
    font-family: "Source Sans 3", Arial, sans-serif;
    color: var(--text);
  }
  .sheet { position: absolute; background: var(--paper); overflow: hidden; }

  .brand {
    display: flex; align-items: center; gap: 6px;
    color: var(--green); font-weight: 600; letter-spacing: -0.3px; white-space: nowrap;
  }
  .brand-dot { border-radius: 50%; background: var(--green); flex: none; }

  .footer-band { position: absolute; left: 0; right: 0; bottom: 0; background: var(--green); }
  .footer-band .band-dark {
    position: absolute; top: 0; bottom: 0; right: 0; background: var(--ink);
    display: flex; align-items: center; justify-content: flex-end;
    color: #fff; letter-spacing: 1.6px;
  }

  .sender { font-size: 9.5px; line-height: 12.6px; color: var(--text); }
  .sender .accent { color: var(--green); }

  /* Letterhead */
  .letterhead { left: 43px; top: 62px; width: 574px; height: 742px; }
  .letterhead .brand { position: absolute; left: 32px; top: 40px; font-size: 40px; }
  .letterhead .brand-dot { width: 14px; height: 14px; }
  .letterhead .sender { position: absolute; right: 22px; top: 57px; text-align: right; }
  .letter-body {
    position: absolute; left: 77px; top: 203px; width: 419px;
    font-size: 9.6px; line-height: 11.2px; text-align: justify;
    hyphens: auto; -webkit-hyphens: auto;
  }
  .letter-body p + p { margin-top: 11.2px; }
  .signature {
    position: absolute; left: 82px; top: 577px; width: 90px; height: 68px;
    background: #ececec; border-radius: 4px;
  }
  .letterhead .footer-band { height: 19px; }
  .letterhead .band-dark {
    width: 222px; padding-right: 60px; font-size: 9.5px;
    clip-path: polygon(18px 0, 100% 0, 100% 100%, 0 100%);
  }

  /* Business card front */
  .card-front { left: 657px; top: 129px; width: 236px; height: 134px; }
  .card-front .brand { position: absolute; left: 13px; top: 14px; font-size: 20px; gap: 4px; }
  .card-front .brand-dot { width: 7px; height: 7px; }
  .card-details { position: absolute; left: 15px; font-size: 5.6px; line-height: 7.6px; color: var(--text); }
  .card-details .accent { color: var(--green); }
  .card-address { top: 70px; }
  .card-contact { top: 106px; }
  .card-front .holder { position: absolute; right: 13px; top: 94px; text-align: right; }
  .holder-name { font-size: 9px; font-weight: 600; color: var(--ink); line-height: 11px; }
  .holder-role { font-size: 6.5px; color: var(--green); line-height: 9px; }
  .card-front .footer-band { height: 7px; }
  .card-front .band-dark { width: 93px; clip-path: polygon(7px 0, 100% 0, 100% 100%, 0 100%); }

  /* Business card back */
  .card-back { left: 908px; top: 130px; width: 236px; height: 134px; background: var(--green); }
  .card-back .brand { position: absolute; right: 11px; top: 85px; font-size: 24px; color: #fff; gap: 5px; }
  .card-back .brand-dot { width: 8px; height: 8px; background: #fff; }
  .card-back .card-url {
    position: absolute; right: 12px; top: 119px; font-size: 7.6px; letter-spacing: 1.8px; color: #fff;
  }

  /* Envelope back with flap */
  .envelope-back { left: 529px; top: 314px; width: 640px; height: 278px; box-shadow: 0 1px 3px rgba(0,0,0,0.25); }
  .envelope-back .flap { position: absolute; left: 0; top: 0; width: 640px; height: 92px; }
  .envelope-back .flap-mark {
    position: absolute; left: 304px; top: 31px; width: 32px; height: 32px;
    border-radius: 50%; background: #fff;
  }

  /* Envelope front */
  .envelope-front { left: 469px; top: 429px; width: 643px; height: 280px; box-shadow: 0 1px 3px rgba(0,0,0,0.3); }
  .envelope-front .brand { position: absolute; left: 17px; top: 20px; font-size: 29px; gap: 5px; }
  .envelope-front .brand-dot { width: 10px; height: 10px; }
  .envelope-front .sender { position: absolute; left: 17px; top: 65px; }
  .envelope-front .footer-band { height: 19px; }
  .envelope-front .band-dark {
    width: 252px; padding-right: 70px; font-size: 9.5px;
    clip-path: polygon(16px 0, 100% 0, 100% 100%, 0 100%);
  }
</style>
</head>
<body>

  <section class="sheet letterhead">
    <div class="brand"><span>Lumo Vance</span><span class="brand-dot"></span></div>
    <div class="sender">
      <div class="accent">Lumo Vance Ltd.</div>
      <div>42 Quarry Lane, London, W1F 7QX</div>
      <div><span class="accent">Phone.</span> 0208 514 6290</div>
    </div>
    <div class="letter-body">
      <p>Lorem ipsum dolor sit amet, consectetuer adipiscing elit. Pellentesque tristique elementum sem. Quisque eget erat ac lectus sodales faucibus. Nam commodo est. Cras consequat faucibus velit. Nam ac magna. Sed et ligula. Nam volutpat, elit ac facilisis tempor, neque augue euismod leo, sit amet molestie sem est eu libero. Nulla facilisi. Pellentesque sit amet odio. Curabitur a leo consectetuer leo blandit porttitor. Pellentesque velit quam, gravida at, pharetra eu, convallis non, sem. Aenean tempor nibh at purus. Pellentesque porta. Suspendisse congue, lacus sit amet imperdiet imperdiet, urna massa rutrum urna, id elementum tellus diam quis risus.</p>
      <p>In dui turpis, varius vitae, tincidunt id, consequat ut, leo. Donec tincidunt tristique odio. Nulla erat felis, euismod nec, fringilla non, aliquet et, magna. Nulla at magna quis nisi pretium vehicula. Pellentesque habitant morbi tristique senectus et netus et malesuada fames ac turpis egestas. Class aptent taciti sociosqu ad litora torquent per conubia nostra, per inceptos himenaeos. In vel quam. Phasellus varius convallis purus. In non turpis. Nam sed risus. Etiam non neque at nisl gravida porttitor. Donec leo dolor, feugiat ut, pharetra et, porttitor a, metus. Suspendisse laoreet magna vel elit. Ut est augue, fermentum ac, molestie at, vestibulum et, urna.</p>
      <p>Nunc purus. Cras auctor. In ornare neque id ipsum. Nulla tincidunt, diam sit amet viverra sapien augue fringilla neque, at pellentesque felis tortor vel enim. Etiam dignissim arcu vel nisl euismod ultricies. Donec molestie congue lectus. Integer sed turpis a tortor consequat. Maecenas molestie placerat urna. Sed pede enim, sollicitudin nec, sollicitudin a, felis. In hac habitasse platea dictumst. Nam facilisis, tellus non sodales erat, turpis turpis semper ante, euismod imperdiet augue nisi et neque. Vivamus.</p>
      <p>Nulla lobortis ultricies nulla. Pellentesque purus mi, consequat quis, hendrerit non, eros. Nullam urna est, vehicula nec, cursus nec, dignissim sit amet, risus. Nam tellus sit amet laoreet ullamcorper, urna nisi fringilla ante, at rhoncus justo dolor hendrerit luctus lorem. Aenean tempor, metus vel posuere gravida, arcu nunc imperdiet blandit sem magna a turpis. Vivamus in neque. Lorem ipsum dolor sit amet, consectetuer adipiscing elit. Duis tristique tortor id nisl feugiat posuere. Maecenas posuere nisi hendrerit. Praesent porta tempus ligula. Morbi in leo. Curabitur sapien nulla, cursus in, porttitor et, odio. Praesent sed justo sed arcu commodo feugiat. Duis facilisis. Cras libero. Donec mollis consectetuer metus. Praesent odio.</p>
    </div>
    <div class="signature" role="img" aria-label="Handwritten signature of the sender"></div>
    <div class="footer-band"><div class="band-dark">www. lumo-vance.it</div></div>
  </section>

  <section class="sheet card-front">
    <div class="brand"><span>Lumo Vance</span><span class="brand-dot"></span></div>
    <div class="card-details card-address">
      <div class="accent">Lumo Vance Ltd.</div>
      <div>42 Quarry Lane</div>
      <div>London, W1F 7QX</div>
    </div>
    <div class="card-details card-contact">
      <div><span class="accent">Phone.</span> 0208 514 6290</div>
      <div><span class="accent">Email.</span> hello@lumo-vance.it</div>
    </div>
    <div class="holder">
      <div class="holder-name">Elric Dawson</div>
      <div class="holder-role">Marketing Manager</div>
    </div>
    <div class="footer-band"><div class="band-dark"></div></div>
  </section>

  <section class="sheet card-back">
    <div class="brand"><span>Lumo Vance</span><span class="brand-dot"></span></div>
    <div class="card-url">www. lumo-vance.it</div>
  </section>

  <section class="sheet envelope-back">
    <svg class="flap" viewBox="0 0 640 92" preserveAspectRatio="none" aria-hidden="true">
      <polygon points="0,0 640,0 640,4 612,80 330,80 320,89 310,80 28,80 0,4" fill="var(--green)"/>
    </svg>
    <div class="flap-mark"></div>
  </section>

  <section class="sheet envelope-front">
    <div class="brand"><span>Lumo Vance</span><span class="brand-dot"></span></div>
    <div class="sender">
      <div class="accent">Lumo Vance Ltd.</div>
      <div>42 Quarry Lane, London, W1F 7QX</div>
      <div><span class="accent">Phone.</span> 0208 514 6290</div>
    </div>
    <div class="footer-band"><div class="band-dark">www. lumo-vance.it</div></div>
  </section>

</body>
</html>
```